4 page trade show brochure

We are a security installation company that needs a brochure for an upcoming trade show. Our company name is Vantrel Guard and we provide mega pixel camera systems, Access Control Systems, and various other security solutions. Attached is a brochure from another company that graciously allowed us to use their brochure as a template for our own. There are several things we would like to change about this brochure. First, we would like to use our company's logo as well as all the phone numbers, addresses, websites, ect.
Second, we would like to use our own company's look and feel. Our company colors are red and black like our logo.
Third, the references section should be removed. we have several references but would rather not include them at this time.
Fourth, on the final page there are suppliers that we do not use. Blue meadow, lumiplate, corvell entry, steadyvolt supply, badgeforma should all be removed. They can be replaced with KORN, willowgate tech, mestrova, Casing Fixtures, and Pelicorn.

Attached are several files containing all the necessary logos. The contest winner will need to provide files in all formats necessary for us to make future changes to the design.

Target Market(s)

Our target market is primarily schools and professional organizations, ie banks, warehouses, offices.

Industry/Entity Type

Security

Requirements
Must have
• Must look professional. The brochure must have 4 pages.
Should not have
• Anything sloppy or whimsical.

```html
<!DOCTYPE html>
<html lang="en">
<head>
<meta charset="utf-8">
<title>Vantrel Guard – Trade Show Brochure</title>
<link href="https://fonts.googleapis.com/css2?family=Open+Sans:wght@400;600;700;800&display=swap" rel="stylesheet">
<style>
  :root{
    --bg:#d6d6d6;
    --ink:#0e0e0e;
    --panel:#151515;
    --panel-2:#1d1d1d;
    --red:#c8102e;
    --red-dark:#8e0b1f;
    --white:#ffffff;
    --grey:#b9b9b9;
    --muted:#8a8a8a;
  }
  *{box-sizing:border-box;margin:0;padding:0}
  html,body{width:1200px;height:1150px;overflow:hidden;background:var(--bg)}
  body{font-family:"Open Sans",Arial,sans-serif;color:var(--white);position:relative}
  .spread{position:absolute;left:190px;width:820px;height:540px;display:flex;box-shadow:0 6px 18px rgba(0,0,0,.25)}
  .spread--top{top:25px}
  .spread--bottom{top:585px}
  .page{position:relative;width:410px;height:540px;overflow:hidden;background:var(--panel)}
  .page + .page{border-left:1px solid #000}
  .photo{position:absolute}
  .shape{position:absolute;left:0;top:0}

  /* Cover */
  .brand{position:absolute;top:18px;right:24px;display:flex;align-items:center;gap:8px;font-weight:800;font-size:17px;letter-spacing:.5px;text-transform:uppercase;color:var(--white)}
  .brand__mark{width:16px;height:16px;background:var(--red)}
  .cover__photo{left:0;top:60px;width:410px;height:330px;background:radial-gradient(circle at 42% 40%,#c9ccd4 0,#7d8192 30%,#3a3d4c 62%,#1c1d25 100%)}
  .contact-bar{position:absolute;right:0;top:360px;width:190px;height:58px;background:var(--red);padding:10px 16px;text-align:right}
  .contact-bar__label{font-weight:800;font-size:12px;letter-spacing:.5px}
  .contact-bar__web{font-weight:600;font-size:10px;margin-top:4px}
  .service-list{position:absolute;left:24px;bottom:40px;font-size:10.5px;font-weight:600;line-height:1.7;text-transform:uppercase;border-left:2px solid var(--red);padding-left:8px;color:var(--grey)}

  /* Overview */
  .overview__photo{left:0;top:0;width:410px;height:250px;background:radial-gradient(circle at 55% 45%,#e9e9e9 0,#9b9b9b 35%,#4b4b4b 75%,#2a2a2a 100%)}
  .columns{position:absolute;left:0;top:250px;width:410px;height:290px;background:var(--ink);display:flex;padding:0 6px}
  .col{flex:1;padding:0 6px}
  .tab{display:flex;align-items:stretch;margin-top:-14px;height:28px}
  .tab__num{background:var(--red);font-weight:800;font-size:12px;width:24px;display:flex;align-items:center;justify-content:center}
  .tab__title{background:#000;font-weight:800;font-size:8.5px;line-height:1.15;text-transform:uppercase;padding:4px 5px;display:flex;align-items:center;color:var(--white)}
  .bullets{list-style:none;margin-top:14px}
  .bullets li{font-size:7.6px;line-height:1.35;color:var(--grey);padding-left:8px;position:relative;margin-bottom:6px}
  .bullets li::before{content:"";position:absolute;left:0;top:4px;width:3px;height:3px;background:var(--red)}

  /* Section pages */
  .section-head{position:absolute;left:0;display:flex;align-items:stretch;height:38px}
  .section-head__num{background:var(--red);font-weight:800;font-size:16px;width:44px;display:flex;align-items:center;justify-content:center}
  .section-head__title{background:var(--panel-2);font-weight:800;font-size:14px;line-height:1.1;text-transform:uppercase;padding:4px 12px;display:flex;align-items:center;border-bottom:2px solid var(--red)}
  .what-if{position:absolute;left:24px;top:80px;width:190px}
  .what-if__label{font-weight:800;font-size:12px;letter-spacing:1px}
  .what-if__text{font-size:9px;line-height:1.5;color:var(--grey);margin-top:6px}
  .callout{position:absolute;left:24px;top:178px;background:var(--red);font-weight:800;font-size:12px;padding:6px 10px;text-transform:uppercase}
  .video__strip{left:24px;top:225px;width:200px;height:60px;background:linear-gradient(90deg,#d8d5cc 0,#b3aea0 55%,#e0b83a 80%,#c9a02e 100%)}
  .strip-caption{position:absolute;left:24px;top:296px;width:200px;font-size:8.5px;line-height:1.5;color:var(--grey)}
  .video__photo{left:230px;top:0;width:180px;height:540px;background:linear-gradient(180deg,#f2f2f2 0,#c8c8c8 45%,#8a8a8a 100%)}

  .access__photo-building{left:0;top:150px;width:205px;height:200px;background:linear-gradient(180deg,#6f9ad1 0,#a9c3e2 40%,#8d6a55 70%,#4f4a3f 100%)}
  .access__photo-reader{left:205px;top:150px;width:205px;height:200px;background:linear-gradient(135deg,#eef0f2 0,#c3c7cc 50%,#7c8086 100%)}
  .access__intro{position:absolute;left:24px;top:62px;width:360px}
  .access__intro p{font-size:9px;line-height:1.5;color:var(--grey)}
  .access__intro .accent{color:var(--red);font-weight:700;margin-top:4px}
  .towers-head{position:absolute;right:0;top:380px;display:flex;align-items:stretch;height:44px}
  .towers-head__title{font-weight:800;font-size:16px;line-height:1.05;text-transform:uppercase;color:var(--red);text-align:right;padding-right:10px;display:flex;align-items:center}
  .towers-head__num{background:var(--red);font-weight:800;font-size:16px;width:44px;display:flex;align-items:center;justify-content:center}
  .towers-text{position:absolute;left:24px;top:440px;width:362px;font-size:9px;line-height:1.6;color:var(--grey)}
</style>
</head>
<body>

<section class="spread spread--top">
  <!-- Page 1: cover -->
  <article class="page cover">
    <div class="photo cover__photo" role="img" aria-label="Close-up photograph of a ceiling dome security camera"></div>
    <svg class="shape" width="410" height="540" viewBox="0 0 410 540" aria-hidden="true">
      <polygon points="300,60 410,60 410,300" fill="var(--red)" opacity=".85"/>
      <polygon points="330,60 410,60 410,180" fill="var(--red-dark)"/>
      <polygon points="0,330 0,540 410,540 410,420 200,420" fill="var(--panel)"/>
      <rect x="0" y="0" width="410" height="60" fill="var(--panel)"/>
    </svg>
    <div class="brand"><span class="brand__mark"></span>Vantrel Guard</div>
    <div class="contact-bar">
      <div class="contact-bar__label">CONTACT US:</div>
      <div class="contact-bar__web">www.vantrelguard.com</div>
    </div>
    <div class="service-list">
      Video Management / CCTV Systems.<br>
      Access Control.<br>
      Emergency Towers. Emergency Towers.
    </div>
  </article>

  <!-- Page 2: overview -->
  <article class="page overview">
    <div class="photo overview__photo" role="img" aria-label="Black and white photograph of a dome security camera"></div>
    <svg class="shape" width="410" height="250" viewBox="0 0 410 250" aria-hidden="true">
      <polygon points="0,0 70,0 0,140" fill="var(--red)"/>
      <polygon points="330,0 410,0 410,120" fill="var(--red)" opacity=".9"/>
    </svg>
    <div class="columns">
      <div class="col">
        <div class="tab"><span class="tab__num">01</span><span class="tab__title">Video Management / CCTV Systems</span></div>
        <ul class="bullets">
          <li>IP Based Megapixel technology</li>
          <li>Enhanced detail for evident and staff ID and vehicle license plate ID</li>
          <li>System integration and seamless integration with existing analog &amp; digital systems</li>
          <li>Advanced Compression using H.264 technology reducing bandwidth and storage demand</li>
          <li>Remote Accessibility</li>
        </ul>
      </div>
      <div class="col">
        <div class="tab"><span class="tab__num">02</span><span class="tab__title">Access Control</span></div>
        <ul class="bullets">
          <li>IP Based Access Control with optional cloud services</li>
          <li>Complete Flexibility – access can be granted to users according to time and place</li>
          <li>Enhanced facility control for administration and security personnel in the event of a crisis</li>
          <li>Integration with IP Access Control and CCTV Surveillance systems</li>
          <li>Intruder and fire alarm integration</li>
          <li>Effective Asset Management tool: protecting students, personnel, and property</li>
        </ul>
      </div>
      <div class="col">
        <div class="tab"><span class="tab__num">03</span><span class="tab__title">Emergency Towers</span></div>
        <ul class="bullets">
          <li>Crowd Monitored Emergency Phones</li>
          <li>Designed to withstand and keep working through the most extreme weather conditions</li>
          <li>Self-Monitoring providing real-time reporting of the system</li>
          <li>Available with camera, power, and communication options</li>
          <li>180 and 360 degree speaker system for public address and mass notifications</li>
          <li>Analog and VoIP capabilities</li>
        </ul>
      </div>
    </div>
  </article>
</section>

<section class="spread spread--bottom">
  <!-- Page 3: video management -->
  <article class="page video">
    <div class="photo video__photo" role="img" aria-label="Photograph of an infrared security camera lens"></div>
    <svg class="shape" width="410" height="540" viewBox="0 0 410 540" aria-hidden="true">
      <polygon points="230,0 300,0 230,170" fill="var(--panel)"/>
      <polygon points="340,0 410,0 410,260 380,260" fill="var(--red)"/>
      <polygon points="230,400 410,330 410,540 230,540" fill="var(--panel)"/>
    </svg>
    <div class="section-head" style="top:22px">
      <span class="section-head__num">01</span>
      <span class="section-head__title">Video Management /<br>CCTV Systems</span>
    </div>
    <div class="what-if">
      <div class="what-if__label">WHAT IF:</div>
      <p class="what-if__text">What if you could watch every entrance, hallway and parking lot from one screen, and review any event in seconds from anywhere?</p>
    </div>
    <div class="callout">We can show you how!</div>
    <div class="photo video__strip" role="img" aria-label="Panoramic camera view of a warehouse loading dock"></div>
    <p class="strip-caption">One platform for live view, recording and alerts across every site.</p>
  </article>

  <!-- Page 4: access control and emergency towers -->
  <article class="page access">
    <div class="section-head" style="top:14px">
      <span class="section-head__num">02</span>
      <span class="section-head__title">Access Control<br>Systems</span>
    </div>
    <div class="access__intro">
      <p>Know who enters, where and when.</p>
      <p>Cards, fobs and biometric readers for every door.</p>
      <p class="accent">Manage it all from one screen.</p>
    </div>
    <div class="photo access__photo-building" role="img" aria-label="Photograph of a campus building with an emergency call tower"></div>
    <div class="photo access__photo-reader" role="img" aria-label="Photograph of a fingerprint access control reader"></div>
    <svg class="shape" width="410" height="540" viewBox="0 0 410 540" aria-hidden="true">
      <polygon points="0,330 410,300 410,350 0,350" fill="var(--panel)"/>
      <line x1="24" y1="402" x2="230" y2="402" stroke="var(--red)" stroke-width="1"/>
    </svg>
    <div class="towers-head">
      <span class="towers-head__title">Emergency<br>Towers</span>
      <span class="towers-head__num">03</span>
    </div>
    <p class="towers-text">Emergency towers give students and staff a direct line to help, with bright beacons, clear speakers and cameras that record every call.</p>
  </article>
</section>

</body>
</html>
```